New Business Card Design Project

I have a logo I would like to use on the business card. I want something that will stand out and that will be remembered.

Target Market(s)

People who collect gems, minerals and crystals.

Contact Information for Business Card

email - mkthestonefalcon@vendrollo.com
phone # 917-406-2581

Font styles to use
Serif
Sans Serif
Decorative

Colors

Designer to choose colors to be used in the design.

Requirements
Must have
• The logo...two to choose from.
Nice to have
• An eye catching and memorable way to draw in people who collect gems minerals and crystals.

```html
<!DOCTYPE html>
<html lang="en">
<head>
<meta charset="utf-8">
<title>The Stone Falcon – Business Card</title>
<link rel="stylesheet" href="https://fonts.googleapis.com/css2?family=Oswald:wght@500&family=Open+Sans:wght@400&display=swap">
<style>
  :root {
    --bg: #202020;
    --card: #242424;
    --card-edge: #2f2f2f;
    --accent: #2f45a8;
    --text-light: #f2f2f2;
  }
  * { margin: 0; padding: 0; box-sizing: border-box; }
  html, body { width: 1200px; height: 926px; overflow: hidden; background: var(--bg); }
  .canvas { position: relative; width: 1200px; height: 926px; }

  .card {
    position: absolute;
    width: 540px;
    height: 309px;
    background: var(--card);
    border: 1px solid var(--card-edge);
    box-shadow: 0 10px 30px rgba(0,0,0,.45);
    overflow: hidden;
  }
  .card::after {
    content: "";
    position: absolute;
    left: 0; right: 0; bottom: 0;
    height: 7px;
    background: var(--accent);
  }
  .card--front { left: 590px; top: 90px; }
  .card--back  { left: 70px;  top: 470px; }

  .brand {
    position: absolute;
    inset: 0 0 7px 0;
    display: flex;
    align-items: center;
    justify-content: center;
    gap: 14px;
  }
  .brand__dot {
    width: 22px; height: 22px;
    border-radius: 50%;
    background: var(--accent);
  }
  .brand__name {
    font-family: "Oswald", sans-serif;
    font-weight: 500;
    font-size: 38px;
    letter-spacing: 2px;
    text-transform: uppercase;
    color: var(--accent);
  }

  .contact-block {
    position: absolute;
    inset: 0 0 7px 0;
    display: flex;
    align-items: center;
    justify-content: center;
    gap: 22px;
  }
  .holder-name {
    font-family: "Oswald", sans-serif;
    font-weight: 500;
    font-size: 34px;
    letter-spacing: 1px;
    text-transform: uppercase;
    color: var(--accent);
  }
  .divider { width: 1.5px; height: 64px; background: var(--text-light); }
  .contact-list { list-style: none; display: flex; flex-direction: column; gap: 6px; }
  .contact-item {
    display: flex; align-items: center; gap: 10px;
    font-family: "Open Sans", sans-serif;
    font-size: 15px;
    color: var(--text-light);
  }
  .contact-item svg { width: 16px; height: 16px; flex: none; }
</style>
</head>
<body>
<main class="canvas">
  <section class="card card--front" aria-label="Card front">
    <div class="brand">
      <span class="brand__dot"></span>
      <span class="brand__name">The Stone Falcon</span>
    </div>
  </section>

  <section class="card card--back" aria-label="Card back">
    <div class="contact-block">
      <h1 class="holder-name">Marco Keller</h1>
      <span class="divider"></span>
      <ul class="contact-list">
        <li class="contact-item">
          <svg viewBox="0 0 24 24" aria-hidden="true"><path fill="var(--accent)" d="M6.6 10.8a15 15 0 0 0 6.6 6.6l2.2-2.2c.3-.3.7-.4 1-.2 1.1.4 2.3.6 3.6.6.6 0 1 .4 1 1V20c0 .6-.4 1-1 1A17 17 0 0 1 3 4c0-.6.4-1 1-1h3.5c.6 0 1 .4 1 1 0 1.3.2 2.5.6 3.6.1.3 0 .7-.2 1z"/></svg>
          <span>917-406-2581</span>
        </li>
        <li class="contact-item">
          <svg viewBox="0 0 24 24" aria-hidden="true"><rect x="2" y="5" width="20" height="14" rx="1" fill="var(--accent)"/><path d="M3 6l9 7 9-7" fill="none" stroke="var(--card)" stroke-width="1.6"/></svg>
          <span>mkthestonefalcon@vendrollo.com</span>
        </li>
      </ul>
    </div>
  </section>
</main>
</body>
</html>
```